New Chartered Accounting Practice Needs Stationery Design

I need a new set of stationery including letterhead, business cards, envelopes and with compliments slips for a new Chartered Accounting Practice based in Melbourne, Victoria, Australia called "Martin K. Ashbury, Chartered Accountant".
I will be providing Taxation Services, Accounting Services, Self-Managed Superannuation Fund Consulting and general consulting advice to small and medium business enterprises. I would like to see designs that use the colour blue. The final design should communicate trust, technical expertise and security.
Target Market(s)
English speaking, Australians. Proprietors of small and medium businesses - aged 30-65. Fellow professionals - lawyers, investment consultants, other accountants. Retirees - aged 60 and over
Industry/Entity Type
Business
Look and feel

```html
<!DOCTYPE html>
<html lang="en">
<head>
<meta charset="utf-8">
<title>Martin K. Ashbury, Chartered Accountant – Business Card</title>
<link href="https://fonts.googleapis.com/css2?family=Cinzel:wght@400;600&family=Raleway:wght@300;400;500&display=swap" rel="stylesheet">
<style>
  :root {
    --page-bg: #e9ecef;
    --card-white: #ffffff;
    --brand-blue: #3aa3c8;
    --brand-blue-deep: #2f93b9;
    --tab-blue: #9dbbd9;
    --text-blue: #3a9cc6;
    --sub-blue: #5aaed0;
    --divider: #e3e6ea;
  }
  * { margin: 0; padding: 0; box-sizing: border-box; }
  html, body { width: 1200px; height: 563px; overflow: hidden; }
  body {
    background: var(--page-bg);
    font-family: "Raleway", Arial, sans-serif;
    position: relative;
  }
  .card {
    position: absolute;
    top: 136px;
    width: 510px;
    height: 292px;
    overflow: hidden;
    box-shadow: 0 6px 18px rgba(0,0,0,0.12);
  }
  .card--front { left: 60px; background: var(--card-white); }
  .card--back { left: 630px; background: var(--brand-blue); }

  .holder-name {
    font-family: "Cinzel", Georgia, serif;
    font-weight: 400;
    letter-spacing: 0.5px;
  }
  .holder-title { font-weight: 300; letter-spacing: 0.6px; }

  /* front */
  .front-identity { position: absolute; left: 38px; top: 98px; color: var(--text-blue); }
  .front-identity .holder-name { font-size: 21px; }
  .front-identity .holder-title { font-size: 15px; color: var(--sub-blue); margin-top: 2px; padding-left: 28px; }
  .front-divider { position: absolute; left: 268px; top: 62px; width: 1px; height: 120px; background: var(--divider); }
  .contact-list {
    position: absolute; left: 284px; top: 62px;
    list-style: none; color: var(--text-blue);
    font-size: 12px; font-weight: 500; line-height: 1.25;
  }
  .contact-list li { display: flex; align-items: flex-start; gap: 6px; margin-bottom: 7px; }
  .contact-list .phones { gap: 14px; }
  .contact-list .phone { display: flex; align-items: center; gap: 6px; }
  .icon { width: 13px; height: 13px; flex: none; fill: var(--text-blue); }
  .front-band { position: absolute; left: 0; top: 210px; width: 510px; height: 36px; }
  .front-web {
    position: absolute; right: 22px; top: 216px;
    display: flex; align-items: center; gap: 6px;
    color: #fff; font-size: 12.5px; font-weight: 500;
  }
  .front-web .icon { fill: #fff; }

  /* back */
  .back-identity { position: absolute; left: 120px; top: 80px; color: #fff; }
  .back-identity .holder-name { font-size: 25px; font-weight: 600; }
  .back-identity .holder-title { font-size: 17px; color: #e4f3f9; padding-left: 70px; margin-top: 2px; }
  .back-stripes { position: absolute; left: 0; top: 0; width: 510px; height: 292px; }
  .back-web {
    position: absolute; right: 34px; top: 180px;
    display: flex; align-items: center; gap: 6px;
    color: #fff; font-size: 13px; font-weight: 500;
  }
  .back-web .icon { fill: #fff; }
</style>
</head>
<body>

<svg width="0" height="0" style="position:absolute" aria-hidden="true">
  <defs>
    <symbol id="i-pin" viewBox="0 0 16 16"><path d="M8 1L1 7.5h2V15h4v-4h2v4h4V7.5h2z"/></symbol>
    <symbol id="i-box" viewBox="0 0 16 16"><path d="M2 6h9v8H2zM11 6l3-3v2h-2v9h2V6z"/><rect x="12" y="1" width="3" height="2"/></symbol>
    <symbol id="i-phone" viewBox="0 0 16 16"><path d="M4 1h8v14H4zM5.5 3v8h5V3zM7 12.5h2v1H7z"/></symbol>
    <symbol id="i-desk" viewBox="0 0 16 16"><path d="M1 5c2-3 12-3 14 0v2h-3V5.5H4V7H1zM3 8h10l2 6H1zM6 9.5v1h1v-1zM9 9.5v1h1v-1zM6 11.5v1h1v-1zM9 11.5v1h1v-1z"/></symbol>
    <symbol id="i-mail" viewBox="0 0 16 16"><path d="M1 3h14v10H1zM2.5 4.5L8 9l5.5-4.5z" fill-rule="evenodd"/></symbol>
    <symbol id="i-globe" viewBox="0 0 16 16"><path d="M8 1a7 7 0 100 14A7 7 0 008 1zm0 1.3c.8.8 1.4 2.1 1.6 3.7H6.4C6.6 4.4 7.2 3.1 8 2.3zM5.1 6H2.6a5.7 5.7 0 013.3-3.3C5.5 3.6 5.2 4.7 5.1 6zm0 1.3c0 .6.1 1.2.2 1.7H2.4a5.7 5.7 0 010-1.7zm1.3 0h3.2c0 .6-.1 1.2-.2 1.7H6.6a9 9 0 01-.2-1.7zm4.5 0h2.7a5.7 5.7 0 010 1.7h-2.9c.1-.5.2-1.1.2-1.7zm2.5-1.3h-2.5c-.1-1.3-.4-2.4-.8-3.3A5.7 5.7 0 0113.4 6zM2.9 10.3h2.6c.2 1 .5 1.8.9 2.5a5.7 5.7 0 01-3.5-2.5zm4 0h2.2c-.3 1.1-.6 1.8-1.1 2.4-.5-.6-.8-1.3-1.1-2.4zm3.6 0h2.6a5.7 5.7 0 01-3.5 2.5c.4-.7.7-1.5.9-2.5z"/></symbol>
  </defs>
</svg>

<section class="card card--front" aria-label="Business card front">
  <div class="front-identity">
    <h1 class="holder-name">Martin K. Ashbury</h1>
    <p class="holder-title">Chartered Accountant</p>
  </div>
  <div class="front-divider"></div>
  <ul class="contact-list">
    <li><svg class="icon"><use href="#i-pin"/></svg><span>18 Larkin Street,<br>Kew VIC 3101</span></li>
    <li><svg class="icon"><use href="#i-box"/></svg><span>PO Box 4410, Kew VIC 3101</span></li>
    <li class="phones">
      <span class="phone"><svg class="icon"><use href="#i-desk"/></svg>0412 508 316</span>
      <span class="phone"><svg class="icon"><use href="#i-phone"/></svg>(03) 9127 4460</span>
    </li>
    <li><svg class="icon"><use href="#i-mail"/></svg><span>martin.ashbury@mailhub.com.au</span></li>
  </ul>
  <svg class="front-band" viewBox="0 0 510 36" aria-hidden="true">
    <polygon points="298,0 510,0 510,26 290,26" fill="var(--tab-blue)"/>
    <polygon points="0,16 300,16 292,32 0,32" fill="var(--brand-blue)"/>
  </svg>
  <div class="front-web"><svg class="icon"><use href="#i-globe"/></svg>ashburyca.com.au</div>
</section>

<section class="card card--back" aria-label="Business card back">
  <svg class="back-stripes" viewBox="0 0 510 292" aria-hidden="true">
    <polygon points="0,160 510,140 510,152 0,172" fill="#ffffff"/>
    <polygon points="0,244 510,216 510,232 0,260" fill="#ffffff"/>
  </svg>
  <div class="back-identity">
    <h2 class="holder-name">Martin K. Ashbury</h2>
    <p class="holder-title">Chartered Accountant</p>
  </div>
  <div class="back-web"><svg class="icon"><use href="#i-globe"/></svg>ashburyca.com.au</div>
</section>

</body>
</html>
```